Business Card Design Project

I run holistic health workshops, speaking engagements, group and 1on1 coaching, cooking classes, and am a speaker and presenter on holistic health topics.

I would like professionally designed business cards using the attached logo. I would like the reverse of the cards to use the leaf pattern blown up large across the back of the card as the design. I'd also like to use the words "mind.body.spirit.nutrition" across the backside of the cards.

The front of the cards should contain the following contact details:
Megan Thorsby-Quill
Founder & President
The Quill Consulting Group
+61 455 903 671
thequillconsultinggroup@mailvessel.example

Target Market(s)

Corporate HR, Health & wellness businesses, upmarket spas, other businesses in the holistic health & wellness fields looking for a speaker/presenter/workshop leader

Industry/Entity Type

Cooking

Requirements
Must have
• Must use the attached design; must use earth tones in line with the logo (browns/greens/blues/tans)

```html
<!DOCTYPE html>
<html lang="en">
<head>
<meta charset="utf-8">
<title>The Quill Consulting Group – Business Card</title>
<link rel="stylesheet" href="https://fonts.googleapis.com/css2?family=Didact+Gothic&display=swap">
<style>
  :root {
    --backdrop: #ecebe7;
    --card: #ffffff;
    --ink: #3d3d3d;
    --ink-soft: #555555;
    --green-deep: #0f8a4a;
    --green-mid: #3fae49;
    --green-light: #8cc63f;
    --green-pale: #b5d98a;
    --shadow: rgba(0, 0, 0, 0.16);
  }
  * { box-sizing: border-box; margin: 0; padding: 0; }
  html, body {
    width: 1200px;
    height: 900px;
    overflow: hidden;
    background: var(--backdrop);
    font-family: "Didact Gothic", "Century Gothic", sans-serif;
    color: var(--ink);
  }
  .canvas {
    position: relative;
    width: 1200px;
    height: 900px;
  }
  .card {
    position: absolute;
    width: 660px;
    height: 377px;
    background: var(--card);
    box-shadow: 0 6px 18px var(--shadow);
  }

  /* Reverse side */
  .card--back { left: 180px; top: 40px; }
  .back-mark {
    position: absolute;
    left: 0; right: 0; top: 70px;
    display: flex;
    flex-direction: column;
    align-items: center;
    gap: 22px;
  }
  .back-mark__dot {
    width: 150px;
    height: 150px;
    border-radius: 50%;
    background: var(--green-mid);
  }
  .back-mark__name {
    font-size: 30px;
    color: var(--green-deep);
    letter-spacing: 0.5px;
  }
  .tagline {
    position: absolute;
    right: 40px;
    bottom: 34px;
    font-size: 30px;
    letter-spacing: 2px;
    color: var(--ink-soft);
  }

  /* Front side */
  .card--front { left: 360px; top: 483px; }
  .brand {
    position: absolute;
    left: 34px;
    top: 40px;
    display: flex;
    align-items: center;
    gap: 12px;
  }
  .brand__dot {
    width: 26px;
    height: 26px;
    border-radius: 50%;
    background: var(--green-mid);
  }
  .brand__name {
    font-size: 22px;
    color: var(--ink);
  }
  .contact {
    position: absolute;
    left: 330px;
    top: 172px;
  }
  .contact__name {
    font-size: 25px;
    letter-spacing: 1.5px;
    text-transform: uppercase;
    color: var(--ink);
  }
  .contact__role {
    font-size: 17px;
    color: var(--ink-soft);
    margin-top: 2px;
  }
  .contact__list {
    list-style: none;
    margin-top: 22px;
    font-size: 16px;
    color: var(--ink);
  }
  .contact__list li {
    display: flex;
    align-items: center;
    gap: 12px;
    margin-bottom: 9px;
    white-space: nowrap;
  }
  .contact__list svg {
    width: 18px;
    height: 14px;
    flex: none;
  }
  .contact__email { font-size: 14.5px; }
</style>
</head>
<body>
<main class="canvas">

  <section class="card card--back" aria-label="Card reverse">
    <div class="back-mark">
      <span class="back-mark__dot"></span>
      <span class="back-mark__name">The Quill Consulting Group</span>
    </div>
    <p class="tagline">mind.body.spirit.nutrition</p>
  </section>

  <section class="card card--front" aria-label="Card front">
    <div class="brand">
      <span class="brand__dot"></span>
      <span class="brand__name">The Quill Consulting Group</span>
    </div>

    <div class="contact">
      <h1 class="contact__name">Megan Thorsby-Quill</h1>
      <p class="contact__role">Founder &amp; President</p>
      <ul class="contact__list">
        <li>
          <svg viewBox="0 0 18 14" aria-hidden="true">
            <rect x="1" y="1" width="16" height="12" rx="1.5" fill="none" stroke="var(--green-mid)" stroke-width="1.6"/>
            <rect x="3.5" y="3" width="3" height="8" rx="1" fill="var(--green-mid)"/>
            <rect x="9" y="3.5" width="6" height="2" fill="var(--green-mid)"/>
            <rect x="9" y="7" width="6" height="4" fill="var(--green-light)"/>
          </svg>
          <span>+61 455 903 671</span>
        </li>
        <li>
          <svg viewBox="0 0 18 14" aria-hidden="true">
            <rect x="1" y="1" width="16" height="12" fill="none" stroke="var(--green-mid)" stroke-width="1.6"/>
            <polyline points="1,1 9,8 17,1" fill="none" stroke="var(--green-mid)" stroke-width="1.6"/>
          </svg>
          <span class="contact__email">thequillconsultinggroup@mailvessel.example</span>
        </li>
      </ul>
    </div>
  </section>

</main>
</body>
</html>
```